Design our branded business card!

We'd love for you to design our business card and come up with a fitting design that reflects the Pivex brand. We're a growing tech startup with big ambitions. We've included our brand guidelines (contain colour palette), logo (EPS vector in CMYK) and old designs to help you on your way.

We'd like to keep the design fairly simple:

* Name
* Phone number
* Email address
* Website (www.pivex.life)
* Twitter (@pivex)
* Address (18 Wexham Row, Leeds, UK, LS9 4ZQ).

This would need to include print and cutting marks.

If you have any questions just let us know!

Target Market(s)

Businesses, Press and our customers!

Industry/Entity Type

Business

Contact Information for Business Card

* Name
* Phone number
* Email address
* Twitter (@pivex)

Font styles to use
Sans Serif

Requirements
Must have
• 1. Must have the Pivex logo included.
• 2. Must use the font 'Brandon Text' in either 'light' or 'thin' (https://www.typevault-demo.com/fonts/qrsfonts/halden-sans/)
• 3. Must use exact colours references from the brand guidelines. Colours outside of the brand guidelines will be discounted. White (transparent) backgrounds are fine.
• 4. Must contain the following information:
• * Name
• * Phone number
• * Email address
• * Website (www.pivex.life)
• * Twitter (@pivex)
• * Address (18 Wexham Row, Leeds, UK, LS9 4ZQ).
Nice to have
• Must use the font 'Brandon Text' in either 'light' or 'thin' (https://www.typevault-demo.com/fonts/qrsfonts/halden-sans/)
Should not have
• Colours outside of the brand guidelines will be discounted. White (transparent) backgrounds are fine.
• Avoid creating icons or including photography.

```html
<!DOCTYPE html>
<html lang="en">
<head>
<meta charset="utf-8">
<title>Pivex business card</title>
<link rel="stylesheet" href="https://fonts.googleapis.com/css2?family=Nunito+Sans:wght@300;400;700&display=swap">
<style>
  :root {
    --backdrop: #2e2826;
    --card: #161616;
    --card-edge: #222222;
    --brand-green: #6abf4b;
    --wordmark-grey: #3a3a3a;
    --front-wordmark: #4a4a4a;
    --text-light: #e8e8e8;
    --divider: #4d4d4d;
  }
  * { box-sizing: border-box; margin: 0; padding: 0; }
  html, body {
    width: 1200px; height: 814px; overflow: hidden;
    background: var(--backdrop);
    font-family: "Nunito Sans", sans-serif;
  }
  .canvas {
    width: 1200px; height: 814px;
    display: flex; align-items: center; justify-content: center; gap: 40px;
  }
  .card {
    width: 520px; height: 298px;
    background: var(--card);
    border: 1px solid var(--card-edge);
    position: relative;
    box-shadow: 0 10px 30px rgba(0,0,0,.35);
  }
  .brand {
    display: flex; align-items: center; gap: 14px;
    position: absolute;
  }
  .brand-dot {
    border-radius: 50%;
    background: var(--brand-green);
  }
  .brand-name {
    font-weight: 300;
    letter-spacing: 1px;
    text-transform: lowercase;
  }
  .card-front .brand { left: 70px; top: 50%; transform: translateY(-50%); }
  .card-front .brand-dot { width: 74px; height: 74px; }
  .card-front .brand-name { font-size: 66px; color: var(--front-wordmark); }

  .card-back .brand { left: 36px; top: 50%; transform: translateY(-50%); gap: 10px; }
  .card-back .brand-dot { width: 46px; height: 46px; }
  .card-back .brand-name { font-size: 40px; color: var(--wordmark-grey); }

  .divider {
    position: absolute; left: 258px; top: 46px; bottom: 46px;
    width: 1px; background: var(--divider);
  }
  .contact {
    position: absolute; left: 282px; top: 62px;
    color: var(--text-light);
    font-size: 15px; line-height: 1.45; font-weight: 400;
  }
  .contact-name {
    color: var(--brand-green); font-weight: 700; font-size: 19px;
    margin-bottom: 2px;
  }
  .address { margin-bottom: 6px; }
  .contact-list { list-style: none; }
  .contact-list li { display: flex; align-items: center; gap: 9px; }
  .contact-icon { width: 13px; height: 13px; flex: none; fill: var(--brand-green); }
</style>
</head>
<body>
<main class="canvas">
  <section class="card card-front" aria-label="Card front">
    <div class="brand">
      <span class="brand-dot"></span>
      <span class="brand-name">pivex</span>
    </div>
  </section>

  <section class="card card-back" aria-label="Card back">
    <div class="brand">
      <span class="brand-dot"></span>
      <span class="brand-name">pivex</span>
    </div>
    <div class="divider"></div>
    <div class="contact">
      <p class="contact-name">Alex Marlow</p>
      <p class="address">18 Wexham Row<br>Leeds, UK, LS9 4ZQ</p>
      <ul class="contact-list">
        <li>
          <svg class="contact-icon" viewBox="0 0 16 16" aria-hidden="true"><path d="M3.5 1.5l2.5 0 1 3.5-1.6 1.2a9 9 0 0 0 4.4 4.4L11 9l3.5 1v2.5c0 1-1 2-2 2A11.5 11.5 0 0 1 1.5 3.5c0-1 1-2 2-2z"/></svg>
          <span>613 280 4571</span>
        </li>
        <li>
          <svg class="contact-icon" viewBox="0 0 16 16" aria-hidden="true"><path d="M1 3h14v10H1z M2 4.2v.4l6 4 6-4v-.4z" fill-rule="evenodd"/></svg>
          <span>name@pivex.life</span>
        </li>
        <li>
          <svg class="contact-icon" viewBox="0 0 16 16" aria-hidden="true"><circle cx="8" cy="8" r="6.5" fill="none" stroke="var(--brand-green)" stroke-width="1.6"/><path d="M1.5 8h13M8 1.5c-3 3.5-3 9.5 0 13M8 1.5c3 3.5 3 9.5 0 13" fill="none" stroke="var(--brand-green)" stroke-width="1.2"/></svg>
          <span>www.pivex.life</span>
        </li>
        <li>
          <svg class="contact-icon" viewBox="0 0 16 16" aria-hidden="true"><circle cx="8" cy="8" r="6.5"/></svg>
          <span>@pivex</span>
        </li>
      </ul>
    </div>
  </section>
</main>
</body>
</html>
```